App-Design für Vergleichsportal für Reparaturen
Zielgruppe
Flickwerkstatt ist das Vergleichsportal für Reparaturen in deiner Nähe. Egal ob du eine Werkstatt für dein Smartphone, Tablet, Laptop, Computer, Smartwatch oder Spielkonsole suchst. Mit uns findest du deine passende Reparaturwerkstat in deiner Nähe mit dem besten Preis für dich. Du kannst dich direkt über unser Portal deinen Reparaturauftrag erhalten und wirst durch unser Sicher Kaufen Käuferschutz und unser MONVIRA Treuhandschutz abgesichert.
Aufgabenstellung
Unter Flickwerkstatt.de kann das aktuelle Design angeschaut werden. Die Farbe sollten übernommen werden.
Über die Startseite kann der Kunde sein Gerät, Service sowie seine Adresse eingeben. Auf der Vergleichsseite bekommt der Kunde die Übersicht welche Reparaturwerkstätten es gibt, zu welche Preisen die ausgewählte Dienstleistung angeboten wird. Wenn der Kunde auf den Button 'Jetzt Online Bestpreis buchen' drückt, dann kommt der Kunde in den Warenkorb. Im Warenkorb können noch weitere Dienstleistungen und Produkte dazugebucht werden. Und anschließend kommt der Kunde in die Kasse und kann der Bestellvorgang beenden. Die Benutzerführung sollte einfach sein. Im Fokus steht die Vergleichsseite. Dort sollte der Kunde ca. 4 Werkstätten auf einen Blick sehen können. Könnte ausschauen wie bei Wahlblick9 in der Kategorie Mobilfunk.
Die Vergleichseite sollte auf jeden Fall folgende Elemente enthalten:
- Entfernung zur Werkstatt in Meter bzw. Kilometer
- Logo der Werkstatt
- Name der Werkstatt
- Bewertungssterne der Werkstatt
- Reparaturzeit und Ersatzeilverfügbarkeit
- Reparaturpreis (Platz sollte auch bei Auswahl von 2 Dienstleistungen vorhanden sein)
- Rabattanzeige
- Qualitätssiegel (noch nicht vorhanden)
- Anzeige von Verknappung (z. B. noch 3 Termin frei)
- Qualitätsmerkmale (z. B. 12 Monate Garantie)
Die Merkmale Öffnungszeiten, Adresse, Kostenpflichtige Zusatzleistungen können aus Platzgründen in den Warenkorbseite wandern außer es gibt eine schöne und einfache Lösung.
In der Warenkorbseite kann dazu auch die Wahlblick9 Seite dienen.
Bei allen sollte auf die Benutzerfreundlichkeit geachtet werden.
Bei offenen Frage stehe ich zur Verfügung und freue mich auf viele Designs.
Vielen DANK im Voraus!

```html
<!DOCTYPE html>
<html lang="de">
<head>
<meta charset="utf-8">
<title>Flickwerkstatt – Werkstatt wählen</title>
<link href="https://fonts.googleapis.com/css2?family=Open+Sans:wght@400;600&display=swap" rel="stylesheet">
<style>
:root{
  --stage:#2b2b2b;
  --teal:#1f4455;
  --green:#8cc43c;
  --green-dark:#6fa52a;
  --red:#d0021b;
  --ink:#222;
  --muted:#555;
  --page:#eef0f2;
  --line:#c9d1d5;
  --star:#f5c518;
  --star-off:#dcdcdc;
  --brand-blue:#4a67b0;
  --brand-orange:#e8731d;
  --brand-red:#d3202b;
}
*{box-sizing:border-box;margin:0;padding:0}
html,body{width:1200px;height:728px;overflow:hidden}
body{background:var(--stage);font-family:"Open Sans",Arial,sans-serif;color:var(--ink);display:flex;justify-content:center}
.screen{width:376px;height:728px;background:var(--page);overflow:hidden;display:block}
.status{background:#fff;height:30px;display:flex;justify-content:space-between;align-items:center;padding:0 16px 0 18px;font-size:14px;font-weight:600}
.status-icons{display:flex;gap:5px;align-items:center}
.topbar{background:#fff;height:58px;display:flex;justify-content:space-between;align-items:center;padding:0 14px 0 14px}
.brand{display:flex;align-items:center;gap:6px;color:var(--teal);font-size:17px}
.brand-dot{width:12px;height:12px;border-radius:50%;background:var(--green)}
.stepper{background:var(--teal);height:62px;position:relative;color:#fff;font-size:9.5px;overflow:hidden}
.stepper-line{position:absolute;top:23px;left:64px;right:62px;height:1px;background:#fff}
.step{position:absolute;top:15px;display:flex;flex-direction:column;align-items:center;width:110px;margin-left:-55px;white-space:nowrap}
.step-dot{width:16px;height:16px;border-radius:50%;border:1px solid #fff;background:var(--teal);font-size:9px;display:flex;align-items:center;justify-content:center;margin-bottom:8px}
.step.is-active{color:var(--green)}
.step.is-active .step-dot{background:var(--green);color:var(--teal);box-shadow:0 0 0 3px rgba(140,196,60,.35);border-color:var(--green)}
.crumbs{display:flex;justify-content:space-between;font-size:9px;padding:12px 12px 12px 29px;color:var(--ink)}
.crumbs a{color:var(--green-dark);text-decoration:none}
.offer{margin:0 12px 10px 29px;background:#fff;border:1px solid var(--line)}
.offer-head{background:var(--teal);color:#fff;font-size:11.5px;height:34px;display:flex;align-items:center;justify-content:center;position:relative}
.offer-head::after{content:"";position:absolute;left:8px;right:8px;bottom:5px;height:1px;background:#fff}
.offer-head .pin{position:absolute;left:8px;top:9px}
.offer-head .flag{position:absolute;right:10px;top:9px}
.offer-body{padding:9px 10px 10px}
.offer-top{display:flex;justify-content:space-between}
.shop-name{font-size:12.5px;margin-bottom:4px}
.shop-logo{display:flex;align-items:center;gap:5px;font-size:16px;font-weight:600;height:24px}
.shop-logo i{width:12px;height:12px;display:block}
.rating{display:flex;align-items:center;gap:2px;margin-top:5px;font-size:12px;color:var(--star)}
.rating span{margin-left:3px}
.price{text-align:right}
.price-old{font-size:17px;text-decoration:line-through;margin-top:4px}
.price-now{font-size:20px;color:var(--red);line-height:1.2}
.price-single{font-size:20px;margin-top:14px}
.discount{display:flex;align-items:center;justify-content:flex-end;gap:4px;font-size:8px;color:var(--green-dark);line-height:1.15;margin-top:2px}
.facts{display:flex;justify-content:space-between;font-size:9px;margin-top:18px}
.facts dl{display:grid;grid-template-columns:62px 1fr;row-gap:2px}
.facts dt{color:var(--muted)}
.perks{list-style:none;display:flex;flex-direction:column;gap:7px}
.perks li{display:flex;align-items:center;gap:5px}
.scarcity{display:flex;justify-content:center;align-items:center;gap:6px;color:var(--red);font-size:11px;margin:16px 0 12px}
.book{display:flex;align-items:center;justify-content:center;gap:10px;background:var(--green);color:#fff;font-size:14.5px;height:34px;width:100%;border:0;font-family:inherit}
.book-gap{margin-top:20px}
</style>
</head>
<body>
<svg width="0" height="0" style="position:absolute">
  <defs>
    <symbol id="star" viewBox="0 0 24 24"><path d="M12 1.5l3.2 6.9 7.5.8-5.6 5.1 1.6 7.4L12 18l-6.7 3.7 1.6-7.4L1.3 9.2l7.5-.8z"/></symbol>
    <linearGradient id="part" x1="0" x2="1"><stop offset="70%" stop-color="#f5c518"/><stop offset="70%" stop-color="#dcdcdc"/></linearGradient>
    <symbol id="pin" viewBox="0 0 12 16"><path d="M6 0a5 5 0 0 1 5 5c0 4-5 11-5 11S1 9 1 5a5 5 0 0 1 5-5z" fill="#fff"/><circle cx="6" cy="5" r="2" fill="#1f4455"/></symbol>
    <symbol id="flag" viewBox="0 0 12 14"><path d="M1 0v14" stroke="#fff" stroke-width="1.5"/><path d="M2 1h9l-2 3 2 3H2z" fill="#fff"/></symbol>
    <symbol id="cart" viewBox="0 0 22 18"><path d="M1 1h3l3 11h11l2-8H5.5M8 8h10" fill="none" stroke="#fff" stroke-width="1.6"/><circle cx="8.5" cy="15.5" r="1.5" fill="#fff"/><circle cx="16.5" cy="15.5" r="1.5" fill="#fff"/></symbol>
    <symbol id="badge" viewBox="0 0 20 20"><circle cx="10" cy="10" r="8.5" fill="none" stroke="#8cc43c" stroke-width="1.5"/><text x="10" y="13.5" font-size="9" text-anchor="middle" fill="#6fa52a" font-family="Arial">%</text></symbol>
    <symbol id="tool" viewBox="0 0 14 14"><path d="M1 8h5v3H1zM6 9h7M9 2v5M7 4h4" fill="none" stroke="#1f4455" stroke-width="1.2"/></symbol>
    <symbol id="shield" viewBox="0 0 14 14"><path d="M7 1l5 2v4c0 3-2.5 5-5 6-2.5-1-5-3-5-6V3z" fill="none" stroke="#1f4455" stroke-width="1.2"/><path d="M4.5 7l2 2 3-3.5" fill="none" stroke="#1f4455" stroke-width="1.2"/></symbol>
    <symbol id="seal" viewBox="0 0 14 14"><circle cx="7" cy="6" r="4.5" fill="none" stroke="#1f4455" stroke-width="1.2"/><path d="M4.5 9.5L3.5 13.5 7 12l3.5 1.5-1-4" fill="none" stroke="#1f4455" stroke-width="1.2"/></symbol>
  </defs>
</svg>

<main class="screen">
  <div class="status">
    <span>9:41</span>
    <span class="status-icons">
      <svg width="17" height="11"><rect x="0" y="8" width="3" height="3" fill="#222"/><rect x="4.5" y="5.5" width="3" height="5.5" fill="#222"/><rect x="9" y="3" width="3" height="8" fill="#222"/><rect x="13.5" y="0" width="3" height="11" fill="#222"/></svg>
      <svg width="15" height="11"><path d="M1 4a9 9 0 0 1 13 0M3.5 6.5a5.5 5.5 0 0 1 8 0" fill="none" stroke="#222" stroke-width="1.6"/><circle cx="7.5" cy="9.3" r="1.6" fill="#222"/></svg>
      <svg width="24" height="11"><rect x=".5" y=".5" width="21" height="10" rx="2.5" fill="none" stroke="#222"/><rect x="2" y="2" width="18" height="7" rx="1.5" fill="#222"/><rect x="22" y="3.5" width="1.5" height="4" fill="#222"/></svg>
    </span>
  </div>

  <header class="topbar">
    <div class="brand"><span class="brand-dot"></span>Flickwerkstatt</div>
    <svg width="24" height="18" aria-label="Menü"><path d="M0 1h24M0 9h24M0 17h24" stroke="#1f4455" stroke-width="1.6"/></svg>
  </header>

  <nav class="stepper">
    <div class="stepper-line"></div>
    <div class="step is-active" style="left:64px"><span class="step-dot">1</span>Werkstatt wählen</div>
    <div class="step" style="left:187px"><span class="step-dot">2</span>Zahlung durchführen</div>
    <div class="step" style="left:314px"><span class="step-dot">3</span>Gerät abgeben</div>
  </nav>

  <div class="crumbs"><span>Fonix 6s / Akku / Lindenhof 1, München</span><a href="#">✎ Adresse ändern</a></div>

  <article class="offer">
    <div class="offer-head"><svg class="pin" width="10" height="13"><use href="#pin"/></svg>246 m von dir entfernt<svg class="flag" width="10" height="12"><use href="#flag"/></svg></div>
    <div class="offer-body">
      <div class="offer-top">
        <div>
          <div class="shop-name">Fixwerk München</div>
          <div class="shop-logo" style="color:var(--brand-blue)"><i style="background:var(--brand-blue)"></i>Fixwerk</div>
          <div class="rating"><svg width="15" height="15" fill="var(--star)"><use href="#star"/></svg><svg width="15" height="15" fill="var(--star)"><use href="#star"/></svg><svg width="15" height="15" fill="var(--star)"><use href="#star"/></svg><svg width="15" height="15" fill="var(--star)"><use href="#star"/></svg><svg width="15" height="15" fill="var(--star)"><use href="#star"/></svg><span>(5/5)</span></div>
        </div>
        <div class="price">
          <div class="price-old">87,00€</div>
          <div class="price-now">79,00€</div>
          <div class="discount"><svg width="18" height="18"><use href="#badge"/></svg><span>-8,00€ Rabatt<br>endet in 13h</span></div>
        </div>
      </div>
      <div class="facts">
        <dl><dt>Adresse:</dt><dd>Ahornweg 3<br>80339 München</dd><dt>Reparaturzeit:</dt><dd>2 Tage</dd><dt>Ersatzteil:</dt><dd>Verfügbar</dd></dl>
        <ul class="perks"><li><svg width="14" height="14"><use href="#tool"/></svg>kostenlos 30 min.</li><li><svg width="14" height="14"><use href="#shield"/></svg>12 Monate Garantie</li><li><svg width="14" height="14"><use href="#seal"/></svg>Muster Siegel</li></ul>
      </div>
      <div class="scarcity"><svg width="18" height="16"><path d="M9 1l8 14H1z" fill="none" stroke="#d0021b" stroke-width="1.4"/><path d="M9 6v4" stroke="#d0021b" stroke-width="1.6"/><circle cx="9" cy="12.3" r=".9" fill="#d0021b"/></svg>nur noch 3 Termine frei !</div>
      <button class="book"><svg width="20" height="17"><use href="#cart"/></svg>Jetzt Online Bestpreis buchen</button>
    </div>
  </article>

  <article class="offer">
    <div class="offer-head"><svg class="pin" width="10" height="13"><use href="#pin"/></svg>762 m von dir entfernt<svg class="flag" width="10" height="12"><use href="#flag"/></svg></div>
    <div class="offer-body">
      <div class="offer-top">
        <div>
          <div class="shop-name">Handyhof München Giesing</div>
          <div class="shop-logo" style="color:var(--brand-orange)"><i style="background:var(--brand-orange);border-radius:50%"></i>Handyhof</div>
          <div class="rating"><svg width="15" height="15" fill="var(--star)"><use href="#star"/></svg><svg width="15" height="15" fill="var(--star)"><use href="#star"/></svg><svg width="15" height="15" fill="var(--star)"><use href="#star"/></svg><svg width="15" height="15" fill="url(#part)"><use href="#star"/></svg><svg width="15" height="15" fill="var(--star-off)"><use href="#star"/></svg><span>(3,7/5)</span></div>
        </div>
        <div class="price"><div class="price-single">82,00€</div></div>
      </div>
      <div class="facts">
        <dl><dt>Adresse:</dt><dd>Ahornweg 3<br>80339 München</dd><dt>Reparaturzeit:</dt><dd>2 Tage</dd><dt>Ersatzteil:</dt><dd>Verfügbar</dd></dl>
        <ul class="perks"><li><svg width="14" height="14"><use href="#tool"/></svg>kostenlos 90 min.</li><li><svg width="14" height="14"><use href="#shield"/></svg>12 Monate Garantie</li><li><svg width="14" height="14"><use href="#seal"/></svg>Muster Siegel</li></ul>
      </div>
      <button class="book book-gap"><svg width="20" height="17"><use href="#cart"/></svg>Jetzt Online Bestpreis buchen</button>
    </div>
  </article>

  <article class="offer">
    <div class="offer-head"><svg class="pin" width="10" height="13"><use href="#pin"/></svg>1,2 km von dir entfernt<svg class="flag" width="10" height="12"><use href="#flag"/></svg></div>
    <div class="offer-body">
      <div class="offer-top">
        <div>
          <div class="shop-name">Kaufeck am Harras</div>
          <div class="shop-logo" style="color:var(--brand-red)"><i style="background:var(--brand-red)"></i>Kaufeck</div>
          <div class="rating"><svg width="15" height="15" fill="var(--star)"><use href="#star"/></svg><svg width="15" height="15" fill="var(--star)"><use href="#star"/></svg><svg width="15" height="15" fill="var(--star)"><use href="#star"/></svg><svg width="15" height="15" fill="var(--star)"><use href="#star"/></svg><svg width="15" height="15" fill="var(--star)"><use href="#star"/></svg><span>(5/5)</span></div>
        </div>
        <div class="price">
          <div class="price-old">100,00€</div>
          <div class="price-now">89,00€</div>
          <div class="discount"><svg width="18" height="18"><use href="#badge"/></svg><span>-11,00€ Rabatt<br>endet in 13h</span></div>
        </div>
      </div>
    </div>
  </article>
</main>
</body>
</html>
```